Prospekt für Exklusive Busreisen zu besonderen Zielen!
Zielgruppe
Unser Prospekt soll, ansprechend und Jung sein aber nicht abstoßend dem älteren Publikum gegenüber. Modern und Spritzig. Es soll Ruhe ausstrahlen aber auch für Familien mit Kindern ein Erlebnis werden.
einmalig... besonders... sorgenfrei...Urlaub von Anfang an ohne Kompromisse…
Ich bin gespannt auf die tollen Entwürfe.
Anbei unser Logo und Busbilder. Weitere Bilder oder Reisebilder benutzen Sie bitte irgendwelche Bilder als Platzhalter.
Mit uns erleben Sie die schönsten Theater und Spielorte Europas, wie Sie sie noch nie erlebt haben!
Unsere exklusiven Bus-Touren richten sich an Menschen mit hohen Erwartungen, die es gewohnt sind auf Ihren Reisen auf nichts zu verzichten. Mit unseren 5 Sterne-Bussen bieten wir Ihnen einen der höchsten Standards der Reisebusbranche. Natürlich werden alle Reisen von einer Servicekraft begleitet, die nicht nur Ihr Ansprechpartner während der Fahrt ist, sondern sich auch mit einem Getränke- und Snack-Service um Ihr Wohl kümmert und sich im hinteren Bereich in der Kids Lounge um die kleineren Gäste kümmert. Spielen, Basteln .. für alles ist gesorgt. Ein bequemer Sitzabstand von 81cm lässt Ihnen viel Bewegungsfreiheit. Mit der verstellbaren Fußstütze können sie sich zurücklehnen und entspannen! Der Stromanschluss zum laden Ihres Smartphones oder Tablets ist natürlich Standard. Darüber hinaus sind unsere Busse mit kostenfreien WiFi-Hotspots ausgerüstet. Sie können also noch während Ihrer Reise Bilder an Ihre Freunde und Verwandte senden, Ihre Emails lesen oder z.B. Ihre Lieblingsmusik streamen.
Auch bei den Hotels machen wir keine Abstriche. Auf allen Mehrtagestouren, die Sie bei uns buchen, werden Sie in mindestens 4 Sterne-Hotels untergebracht. Bei der Auswahl der Unterkünfte achten wir natürlich darauf, dass diese der Reise angepasst sind. D.h. bei z.B. Städtereisen möglichst zentrumsnah und bei Konzertre..
Aufgabenstellung
32 Seiten, A4 Quadrat,
Datenformat (inkl. 2,00 mm Beschnitt): 21,40 x 21,40 cm
Endformat (offen): 42,00 x 21,00 cm
Endformat (geschlossen): 21,00 x 21,00 cm

```html
<!DOCTYPE html>
<html lang="de">
<head>
<meta charset="utf-8">
<title>Exklusive Busreisen – Karl Wendt Bühnentechnik</title>
<link rel="stylesheet" href="https://fonts.googleapis.com/css2?family=Kaushan+Script&family=Tenor+Sans&family=Source+Sans+3:wght@400;600&display=swap">
<style>
  :root {
    --sky-deep: #7fa6c4;
    --sky-mid: #b9d0e2;
    --sky-light: #e6eef5;
    --globe-edge: #9fbfd8;
    --globe-core: #f4f8fb;
    --paper: #ffffff;
    --accent-orange: #ec7a14;
    --ink-dark: #161616;
    --contact-blue: #1d5ea8;
  }
  * { margin: 0; padding: 0; box-sizing: border-box; }
  html, body { width: 1200px; height: 1200px; overflow: hidden; background: var(--paper); }
  .cover { position: relative; width: 1200px; height: 1200px; background: var(--paper); overflow: hidden; }

  .hero {
    position: absolute; left: 0; top: 0; width: 1200px; height: 852px; overflow: hidden;
    background: linear-gradient(100deg, var(--sky-deep) 0%, var(--sky-mid) 35%, var(--sky-light) 65%, var(--paper) 100%);
  }
  .hero-globe { position: absolute; left: 0; top: 0; width: 1200px; height: 852px; }

  .hero-title {
    position: absolute; left: 150px; top: 118px; width: 920px;
    font-family: "Kaushan Script", cursive; font-weight: 400;
    font-size: 80px; line-height: 1; color: var(--accent-orange);
    transform: rotate(-10deg); transform-origin: left center;
    letter-spacing: 3px; white-space: nowrap;
  }

  .brand-name, .brand-trade {
    position: absolute; left: 0; width: 1200px; text-align: center;
    font-family: "Tenor Sans", sans-serif; color: var(--ink-dark);
  }
  .brand-name { top: 358px; font-size: 54px; letter-spacing: 17px; padding-left: 17px; -webkit-text-stroke: 1px var(--ink-dark); }
  .brand-trade { top: 668px; font-size: 40px; letter-spacing: 3px; -webkit-text-stroke: 0.8px var(--ink-dark); }

  .tagline-band {
    position: absolute; left: 0; top: 852px; width: 1200px; height: 36px;
    background: var(--accent-orange);
    display: flex; align-items: center; justify-content: center;
    font-family: "Source Sans 3", sans-serif; font-size: 22px;
    font-variant: small-caps; letter-spacing: 5px; color: var(--paper);
  }

  .contact {
    position: absolute; left: 0; top: 1022px; width: 1200px; text-align: center;
    font-family: "Source Sans 3", sans-serif; font-style: normal; color: var(--contact-blue);
    font-size: 27px; line-height: 33px;
  }
  .contact-company { font-weight: 600; }
</style>
</head>
<body>
  <main class="cover">
    <div class="hero">
      <svg class="hero-globe" viewBox="0 0 1200 852" role="img" aria-label="Globus mit Längen- und Breitengraden vor hellblauem Himmel">
        <defs>
          <radialGradient id="globe-fill" cx="0.58" cy="0.5" r="0.55">
            <stop offset="0" stop-color="var(--globe-core)"/>
            <stop offset="0.6" stop-color="var(--sky-light)"/>
            <stop offset="1" stop-color="var(--globe-edge)"/>
          </radialGradient>
        </defs>
        <circle cx="690" cy="430" r="470" fill="url(#globe-fill)"/>
      </svg>
    </div>

    <h1 class="hero-title">Exklusive Busreisen</h1>

    <div class="brand-name">KARL WENDT</div>
    <div class="brand-trade">BÜHNENTECHNIK</div>

    <div class="tagline-band">Exklusive Busreisen zu besonderen Zielen</div>

    <address class="contact">
      <div class="contact-company">Karl Wendt Bühnentechnik</div>
      <div>Beispielstraße 2 • 12345 Musterstadt • Telefon +49&nbsp; 123 456789</div>
      <div>info@wendt-reisen.de • www.wendt-reisen.de</div>
    </address>
  </main>
</body>
</html>
```